Business Card Design for Orthopaedic Surgeon

This is a double-sided glossy business card. I prefer baby blue, teal, and green as color schemes. I have my logo already (many colors that you can choose from). I have photos and examples of my old card (very bland but has the information in it). I also have one that my assistant tried to design, but the writing is too small and I don't love the formatting. But it is close!
I would like my logo to be on the business card but I'm uploading my logo in many different colors so you can choose which one looks best based on the color scheme. I also uploaded many sized headshots so you can choose the best resolution one.

Additional information:
Correct business address:
4382 NW 58th Lane, Suite 305
Tamarac, FL 33417

Everything else on both business cards are accurate.

I actually need 2 different business cards generated. One that includes my cell phone number-- Personal cell: 585-314-9062 in addition to Office phone: (954) 316-4870 and Office Fax: 954-316-4881. Again, one card would have my personal cell and one wouldn't

Overall I just think the baby blue card (uploaded) is missing something on the front--of course it is also missing my office phone/fax/personal cell. I do want my website on the front too. Email: info@wellsorthocare.example

You can use your discretion about what goes on the front vs. what goes on the back to eliminated clutter.

Oh and on the back, I would like to list "Conditions Treated" (not specialties include). The list is:
Carpal Tunnel
Trigger Finger
Ganglion Cysts
Hand Tumors
Han & Wrist Arthritis
Hand, Wrist & Elbow Tendonitis
Fractures of the Hand, Wrist, Elbow and Humerus
Nerve Injuries of the Hand, Wrist & Elbow
Microsurgery
Wrist Arthroscopy
Endoscopic Surgery

Target Market(s)

Primary care doctors, Lawyers, patients

Industry/Entity Type

Medical

Contact Information for Business Card

Please see above in project description

Colors

Designer to choose colors to be used in the design.

Requirements
Must have
• -Correct office info, Board Certified Orthopaedic Hand & Upper Extremity Surgeon
Nice to have
• Something that is classy and wow!

```html
<!DOCTYPE html>
<html lang="en">
<head>
<meta charset="utf-8">
<title>Wells Hand – Business Card</title>
<link rel="stylesheet" href="https://fonts.googleapis.com/css2?family=Montserrat:wght@400;500;800&display=swap">
<style>
  :root {
    --backdrop: #d9d9d9;
    --navy: #06161f;
    --teal: #008b8a;
    --gold: #d5b66c;
    --gold-light: #ead596;
    --gold-deep: #b8974d;
    --ink: #1b1b1b;
  }
  * { box-sizing: border-box; margin: 0; padding: 0; }
  html, body { width: 1200px; height: 846px; overflow: hidden; }
  body {
    background: var(--backdrop);
    font-family: "Montserrat", sans-serif;
    display: flex;
    align-items: center;
    justify-content: center;
    gap: 40px;
  }
  .card {
    position: relative;
    width: 560px;
    height: 320px;
    overflow: hidden;
    box-shadow: 0 10px 24px rgba(0,0,0,.18);
  }

  /* shared bottom band */
  .card-rule {
    position: absolute;
    left: 0; right: 0;
    bottom: 46px;
    height: 1px;
    background: var(--gold);
  }
  .card-band {
    position: absolute;
    left: 0; right: 0; bottom: 0;
    height: 38px;
    background: linear-gradient(90deg, var(--gold-deep), var(--gold-light) 45%, var(--gold) 100%);
    display: flex;
    align-items: center;
    justify-content: center;
  }

  /* brand lockup */
  .brand {
    display: flex;
    align-items: center;
    gap: 10px;
    color: var(--gold);
    font-weight: 500;
    letter-spacing: .18em;
    font-size: 17px;
    white-space: nowrap;
  }
  .brand-dot {
    width: 26px; height: 26px;
    border: 2px solid var(--gold);
    border-radius: 50%;
    flex: none;
  }

  /* front */
  .card-front { background: var(--navy); }
  .portrait {
    position: absolute;
    top: 0; right: 0;
    width: 175px; height: 273px;
    background:
      linear-gradient(90deg, var(--navy) 0%, rgba(6,22,31,0) 35%),
      linear-gradient(160deg, #2a1c16 0%, #6b4332 40%, #1b1b1d 75%, #0f0f12 100%);
  }
  .card-front .brand {
    position: absolute;
    left: 20px;
    top: 96px;
    width: 156px;
    flex-direction: column;
    gap: 12px;
    font-size: 15px;
    letter-spacing: .16em;
  }
  .card-front .brand-dot { width: 52px; height: 52px; }
  .contact {
    position: absolute;
    left: 190px;
    top: 72px;
    color: var(--gold);
    font-size: 11px;
    line-height: 1.6;
  }
  .contact-name {
    font-weight: 800;
    font-size: 16px;
    letter-spacing: .02em;
    margin-bottom: 2px;
  }
  .address {
    color: var(--ink);
    font-size: 14px;
    font-weight: 500;
  }

  /* back */
  .card-back { background: var(--teal); }
  .card-back .brand { position: absolute; left: 50%; top: 46px; transform: translateX(-50%); }
  .section-head {
    position: absolute;
    left: 30px; right: 30px;
    top: 122px;
    height: 1px;
    background: var(--gold);
  }
  .section-label {
    position: absolute;
    left: 50%;
    top: -11px;
    transform: translateX(-50%);
    background: var(--teal);
    border: 1px solid var(--gold);
    border-radius: 12px;
    padding: 4px 12px;
    color: var(--gold);
    font-weight: 800;
    font-size: 11px;
    letter-spacing: .02em;
    white-space: nowrap;
  }
  .conditions {
    position: absolute;
    left: 26px; right: 26px;
    top: 146px;
    display: grid;
    grid-template-columns: 1fr 1fr 1fr;
  }
  .conditions ul {
    list-style: none;
    color: var(--gold);
    font-size: 10.5px;
    line-height: 1.45;
    padding: 0 10px;
  }
  .conditions ul + ul { border-left: 1px solid var(--gold); }
  .conditions li { padding-left: 9px; position: relative; }
  .conditions li::before { content: "·"; position: absolute; left: 0; }
</style>
</head>
<body>

  <section class="card card-front">
    <div class="portrait" role="img" aria-label="Headshot portrait of the surgeon in a dark blazer"></div>
    <div class="brand"><span class="brand-dot"></span>WELLS HAND</div>
    <div class="contact">
      <p class="contact-name">DANA WELLS, MD</p>
      <p>Personal cell: 585-314-9062</p>
      <p>Office phone: (954) 316-4870</p>
      <p>Office fax: 954-316-4881</p>
      <p>Email: info@wellsorthocare.example</p>
      <p>www.wellsorthocare.example</p>
    </div>
    <div class="card-rule"></div>
    <div class="card-band">
      <p class="address">4382 NW 58th Lane, Suite 305, Tamarac, FL 33417</p>
    </div>
  </section>

  <section class="card card-back">
    <div class="brand"><span class="brand-dot"></span>WELLS HAND</div>
    <div class="section-head"><span class="section-label">CONDITIONS TREATED</span></div>
    <div class="conditions">
      <ul>
        <li>Carpal Tunnel</li>
        <li>Trigger Finger</li>
        <li>Ganglion Cysts</li>
        <li>Hand Tumors</li>
        <li>Han &amp; Wrist Arthritis</li>
      </ul>
      <ul>
        <li>Hand, Wrist &amp; Elbow Tendonitis</li>
        <li>Fractures of the Hand, Wrist, Elbow and Humerus</li>
      </ul>
      <ul>
        <li>Nerve Injuries of the Hand, Wrist &amp; Elbow</li>
        <li>Microsurgery</li>
        <li>Wrist Arthroscopy</li>
        <li>Endoscopic Surgery</li>
      </ul>
    </div>
    <div class="card-rule"></div>
    <div class="card-band"></div>
  </section>

</body>
</html>
```